Brimlow Oakville Cabernet Sauvignon-Wine label design

We need a package design for an up market wine brand named, Brimlow. It will be a Cabernet Sauvignon from the Oakville AVA of Napa Valley. We are looking for a stylish modern label that will stand out on a retail shelf. We want the label to be attention grabbing and stylish while presenting an up market luxury brand.
Updates

Sick

Requirements
Must have
• Must have the words(in order of importance)
-Brimlow
-Cabernet Sauvignon
-Oakville
-Napa Valley
-2018

Must be designed for a traditional "Bordeaux" style bottle (Bottle specs in uploaded files)
Should not have
• Any images of grapes, vineyards, wine glasses or bottles

```html
<!DOCTYPE html>
<html lang="en">
<head>
<meta charset="utf-8">
<title>Brimlow 2018 Cabernet Sauvignon — Label</title>
<link href="https://fonts.googleapis.com/css2?family=Libre+Caslon+Text:wght@400&display=swap" rel="stylesheet">
<style>
  :root {
    --label-black: #000000;
    --ink-white: #ffffff;
    --band-text: #111111;
    --leaf-green: #2f8a5a;
    --leaf-lime: #b8d434;
    --petal-orange: #f39a2e;
    --petal-magenta: #c9236b;
    --petal-red: #d8352a;
    --water-blue: #3d74c4;
  }
  html, body {
    margin: 0;
    padding: 0;
    width: 773px;
    height: 1200px;
    overflow: hidden;
    background: var(--label-black);
  }
  .label {
    position: relative;
    width: 773px;
    height: 1200px;
    background: var(--label-black);
    color: var(--ink-white);
    font-family: "Libre Caslon Text", "Times New Roman", serif;
  }
  .label__brand {
    position: absolute;
    top: 186px;
    left: 0;
    width: 100%;
    margin: 0;
    text-align: center;
    font-size: 66px;
    font-weight: 400;
    letter-spacing: 6px;
    line-height: 1;
  }
  .label__vintage {
    position: absolute;
    top: 290px;
    left: 247px;
    width: 278px;
    height: 23px;
    background: var(--ink-white);
    color: var(--band-text);
    text-align: center;
    font-size: 19px;
    line-height: 24px;
  }
  .label__varietal {
    position: absolute;
    top: 326px;
    left: 0;
    width: 100%;
    margin: 0;
    text-align: center;
    font-size: 21px;
    font-weight: 400;
    line-height: 1;
  }
  .label__origin {
    position: absolute;
    top: 358px;
    left: 0;
    width: 100%;
    margin: 0;
    text-align: center;
    font-size: 15px;
    line-height: 1;
  }
  .label__origin-dot {
    display: inline-block;
    width: 4px;
    height: 4px;
    margin: 0 8px 3px;
    border-radius: 50%;
    background: var(--ink-white);
  }
  .label__artwork {
    position: absolute;
    left: 0;
    top: 0;
  }
</style>
</head>
<body>
  <main class="label">
    <svg class="label__artwork" width="773" height="1200" viewBox="0 0 773 1200" role="img" aria-label="Colourful stylised illustration of tropical leaves and flame-like petals in green, yellow, orange, magenta and blue">
      <defs>
        <linearGradient id="foliage-gradient" x1="0" y1="0" x2="1" y2="1">
          <stop offset="0" stop-color="var(--leaf-green)"/>
          <stop offset="0.3" stop-color="var(--leaf-lime)"/>
          <stop offset="0.5" stop-color="var(--petal-orange)"/>
          <stop offset="0.7" stop-color="var(--petal-magenta)"/>
          <stop offset="0.88" stop-color="var(--petal-red)"/>
          <stop offset="1" stop-color="var(--water-blue)"/>
        </linearGradient>
      </defs>
      <path d="M61 418 C85 412 105 414 120 422 C160 440 185 455 201 473 C245 520 280 555 311 572 C350 592 385 600 410 616 C520 680 600 720 641 770 C690 840 710 910 712 990 L712 1179 L61 1179 Z" fill="url(#foliage-gradient)"/>
    </svg>

    <h1 class="label__brand">BRIMLOW</h1>
    <div class="label__vintage">2018</div>
    <h2 class="label__varietal">CABERNET SAUVIGNON</h2>
    <p class="label__origin">Napa Valley<span class="label__origin-dot"></span>Oakville</p>
  </main>
</body>
</html>
```